new business card design - modern, professional, bold, B2B focus - with QR code pls

we are looking for a modern looking, colorful, business card design. some highlights:
- put space for QR code please. probably on the back but I'm open.
- biz card to be orientated VERTICAL not the traditional horizontal.
- do NOT use our full name on the card (ie: Allied Furnace Servicing Inc). Use only AFS Inc or AFS.
- use black and orange with some white. ideally black card with orange and white for the letters/logo etc. gray ok too - for outlines etc.
- we work in HEAVY industrial, so the cards should lend itself to this. our website is alfurnace.example, so you can see what we do.
- do NOT put in little smoke stack pictures / silouettes etc.
- think MODERN and INDUSTRIAL, with a techy focus.

Industry/Entity Type

heavy industrial - all of them. we perform maintenance and inspection services at heavy industrial and commercial businesses. so B2B

Contact Information for Business Card

name, title, phone numbers (cell + hardline), website, email address. of course our logo too - either on front or front and back.

Font styles to use
Other font styles liked:
• montserrat

Colors
F0912C
F2A743
F7CA91
FBE8D2
FDF5EE

Requirements
Must have
• see description
Nice to have
• see description
Should not have
• see description

```html
<!DOCTYPE html>
<html lang="en">
<head>
<meta charset="utf-8">
<title>AFS Inc – Business Card</title>
<link href="https://fonts.googleapis.com/css2?family=Montserrat:wght@300;400;500;700;800&display=swap" rel="stylesheet">
<style>
  :root {
    --stage: #5a5a5c;
    --card-black: #221e1f;
    --card-grey: #3b3b3d;
    --orange: #f0912c;
    --orange-light: #f2a743;
    --orange-pale: #f7ca91;
    --orange-deep: #b8600f;
    --text-light: #e9e6e2;
  }
  * { box-sizing: border-box; margin: 0; padding: 0; }
  html, body { width: 1200px; height: 900px; overflow: hidden; }
  body {
    background: var(--stage);
    font-family: "Montserrat", sans-serif;
    position: relative;
  }
  .card {
    position: absolute;
    top: 152px;
    width: 340px;
    height: 595px;
    background: var(--card-black);
    overflow: hidden;
    box-shadow: 0 14px 30px rgba(0,0,0,.35);
  }
  .card--front { left: 225px; }
  .card--back { left: 635px; }
  .card__shapes { position: absolute; inset: 0; width: 100%; height: 100%; }
  .brand-name {
    position: absolute;
    font-weight: 800;
    color: var(--orange);
    letter-spacing: 2px;
    line-height: 1;
  }
  .card--front .brand-name { top: 95px; left: 0; right: 0; text-align: center; font-size: 78px; }
  .card--back .brand-name { top: 80px; left: 60px; font-size: 74px; }
  .contact {
    position: absolute;
    left: 36px;
    top: 388px;
    color: var(--text-light);
  }
  .contact__name {
    font-size: 21px;
    font-weight: 700;
    color: var(--orange);
    letter-spacing: .3px;
  }
  .contact__title {
    font-size: 15px;
    font-weight: 400;
    margin-top: 2px;
  }
  .contact__list { list-style: none; margin-top: 28px; }
  .contact__item {
    display: flex;
    align-items: center;
    gap: 10px;
    font-size: 14.5px;
    font-weight: 400;
    height: 24px;
  }
  .contact__icon { width: 15px; height: 15px; flex: none; }
  .website-vertical {
    position: absolute;
    right: 14px;
    top: 330px;
    writing-mode: vertical-rl;
    color: var(--orange);
    font-size: 13px;
    font-weight: 300;
    letter-spacing: 5px;
  }
  .qr-space {
    position: absolute;
    left: 100px;
    top: 400px;
    width: 120px;
    height: 120px;
    border: 2px dashed var(--orange-pale);
    border-radius: 4px;
    background: rgba(255,255,255,.04);
  }
</style>
</head>
<body>

<section class="card card--front">
  <svg class="card__shapes" viewBox="0 0 340 595" preserveAspectRatio="none">
    <defs>
      <linearGradient id="metal-front" x1="0" y1="0" x2="1" y2="0.15">
        <stop offset="0" stop-color="var(--orange-deep)"/>
        <stop offset=".25" stop-color="var(--orange-light)"/>
        <stop offset=".45" stop-color="var(--orange-deep)"/>
        <stop offset=".65" stop-color="var(--orange)"/>
        <stop offset=".85" stop-color="var(--orange-pale)"/>
        <stop offset="1" stop-color="var(--orange)"/>
      </linearGradient>
    </defs>
    <polygon points="0,245 340,278 340,290 105,290 0,350" fill="url(#metal-front)"/>
    <polygon points="0,358 110,296 340,296 340,595 0,595" fill="var(--card-grey)"/>
    <polyline points="0,354 107,293 340,293" fill="none" stroke="var(--orange)" stroke-width="2"/>
  </svg>
  <div class="brand-name">AFS</div>
  <div class="contact">
    <div class="contact__name">DALE HARTLEY</div>
    <div class="contact__title">CEO &amp; Director</div>
    <ul class="contact__list">
      <li class="contact__item">
        <svg class="contact__icon" viewBox="0 0 16 16"><rect x="4" y="1" width="8" height="14" rx="1.5" fill="none" stroke="var(--orange)" stroke-width="1.4"/><line x1="7" y1="12.5" x2="9" y2="12.5" stroke="var(--orange)" stroke-width="1.2"/></svg>
        555-214-0387
      </li>
      <li class="contact__item">
        <svg class="contact__icon" viewBox="0 0 16 16"><path d="M3 1.5l3 3-1.6 2a8 8 0 0 0 5.1 5.1l2-1.6 3 3-2 2C6.5 15 1 9.5 1 3.5z" fill="var(--orange)"/></svg>
        800-FURNACE
      </li>
      <li class="contact__item">
        <svg class="contact__icon" viewBox="0 0 16 16"><rect x="1" y="3" width="14" height="10" fill="var(--orange)"/><polyline points="1,3 8,9 15,3" fill="none" stroke="var(--card-grey)" stroke-width="1.3"/></svg>
        afsinc@alfurnace.example
      </li>
      <li class="contact__item">
        <svg class="contact__icon" viewBox="0 0 16 16" fill="none" stroke="var(--orange)" stroke-width="1.2"><circle cx="8" cy="8" r="6.5"/><ellipse cx="8" cy="8" rx="3" ry="6.5"/><line x1="1.5" y1="8" x2="14.5" y2="8"/></svg>
        alfurnace.example
      </li>
    </ul>
  </div>
</section>

<section class="card card--back">
  <svg class="card__shapes" viewBox="0 0 340 595" preserveAspectRatio="none">
    <defs>
      <linearGradient id="metal-back" x1="0" y1="1" x2="1" y2="0">
        <stop offset="0" stop-color="var(--orange)"/>
        <stop offset=".3" stop-color="var(--orange-deep)"/>
        <stop offset=".55" stop-color="var(--orange-light)"/>
        <stop offset=".75" stop-color="var(--orange-deep)"/>
        <stop offset="1" stop-color="var(--orange-pale)"/>
      </linearGradient>
    </defs>
    <polygon points="340,150 340,294 166,294 0,464 0,420" fill="url(#metal-back)"/>
    <polygon points="0,476 172,302 340,302 340,595 0,595" fill="var(--card-grey)"/>
    <polyline points="0,470 169,298 340,298" fill="none" stroke="var(--orange)" stroke-width="2"/>
  </svg>
  <div class="brand-name">AFS</div>
  <div class="qr-space" role="img" aria-label="Space reserved for QR code"></div>
  <div class="website-vertical">alfurnace.example</div>
</section>

</body>
</html>
```